Tri fold brochure for construction company

Looking for a tri fold brochure which utilizes black, teal and white colors. Logo must be on main page (several files with Logo attached)
Inside brochure.
1st Page - 3D photo/sketch/drawing of a complete residential high rise building with windows, balconies and elements of concrete and bricks.
2nd Page - Text which will outline company's main activities. file with text is attached.
3rd Page - photo/sketch/drawing of underground parking garage which shows columns/beams/walls/ and garage entrance/exit ramp. Can be multiple photos.
Back of brochure
1st page - company logo
2nd page - please propose something.
3rd page - company message with address and contact info (to be provided)
Back ground color of brochure should complement our logo/photos/sketches/drawings.
Alternative design options are welcome.

```html
<!DOCTYPE html>
<html lang="en">
<head>
<meta charset="UTF-8">
<title>Meridian Restoration Corp – Tri-fold Brochure</title>
<link href="https://fonts.googleapis.com/css2?family=Montserrat:wght@600;700;800&family=Open+Sans:wght@400;600;700&display=swap" rel="stylesheet">
<style>
  :root{
    --teal:#16a58d;
    --teal-dark:#0f8572;
    --black:#1b1b1b;
    --charcoal:#2a2a2a;
    --white:#ffffff;
    --paper:#f4f4f4;
    --grey-text:#5a5a5a;
    --stage:#e3e3e3;
  }
  *{box-sizing:border-box;margin:0;padding:0}
  html,body{width:1200px;height:2400px;overflow:hidden;background:var(--stage)}
  body{position:relative;font-family:"Open Sans",Arial,sans-serif;color:var(--black)}
  .spread{position:absolute;left:45px;width:1110px;height:858px;display:flex;box-shadow:0 12px 30px rgba(0,0,0,.18)}
  .spread--outside{top:240px}
  .spread--inside{top:1300px}
  .panel{position:relative;width:370px;height:100%;overflow:hidden}
  .panel svg.deco{position:absolute;left:0;width:100%}
  .photo{position:absolute;left:0;width:100%}

  /* ---------- outside: services panel ---------- */
  .services{background:var(--paper)}
  .services .photo{top:0;height:300px;background:linear-gradient(160deg,#3a4c6e 0%,#8a7a66 55%,#c9b596 100%)}
  .services .tab{position:absolute;top:330px;left:0;width:170px;height:34px;background:var(--teal);color:var(--white);font:600 16px "Montserrat",Arial,sans-serif;padding:7px 0 0 26px;border-radius:0 18px 18px 0}
  .services .intro{position:absolute;top:382px;left:26px;width:318px;font-size:12.5px;line-height:1.5;color:var(--grey-text);font-style:italic}
  .services ul{position:absolute;top:470px;left:26px;list-style:none;font-size:13px;line-height:1.95;color:var(--grey-text)}
  .services li::before{content:"•";color:var(--teal);margin-right:8px}
  .services .foot{position:absolute;bottom:0;left:0;width:100%;height:40px;background:var(--black);color:var(--white);font:600 13px "Montserrat",Arial,sans-serif;letter-spacing:.5px;padding:12px 0 0 26px;border-top:4px solid var(--teal)}

  /* ---------- outside: teal middle panel ---------- */
  .about{background:var(--teal);color:var(--white);text-align:center}
  .about .circle-photo{position:absolute;top:32px;left:105px;width:160px;height:160px;border-radius:50%;border:6px solid var(--white);background:linear-gradient(135deg,#f2f2f2 0%,#cfd8dc 60%,#9aa6aa 100%)}
  .brand{display:flex;align-items:center;gap:12px;font-family:"Montserrat",Arial,sans-serif;font-weight:800;letter-spacing:.5px}
  .brand .mark{flex:none;width:38px;height:38px}
  .about .brand{position:absolute;top:250px;left:40px;width:290px;font-size:22px;line-height:1.1;color:var(--white);text-align:left}
  .about .brand .mark{background:var(--white)}
  .about p{position:absolute;left:34px;width:302px;font-size:12.5px;line-height:1.55;text-align:left}
  .about .p1{top:350px}
  .about .p2{top:452px}
  .about .cta{position:absolute;top:575px;left:20px;width:330px;font:700 17px/1.35 "Montserrat",Arial,sans-serif;text-transform:uppercase}
  .about .social{position:absolute;top:655px;left:0;width:100%;display:flex;justify-content:center;gap:14px}
  .about .social span{width:24px;height:24px;border-radius:50%;border:2px solid var(--white)}
  .about .phone-bar{position:absolute;bottom:0;left:0;width:100%;height:96px;color:var(--white);font:600 20px "Montserrat",Arial,sans-serif;display:flex;align-items:flex-end;justify-content:center;gap:10px;padding-bottom:26px}

  /* ---------- outside: cover ---------- */
  .cover{background:var(--white)}
  .cover .brand{position:absolute;top:64px;left:40px;width:300px;font-size:20px;line-height:1.15;color:var(--black)}
  .cover .brand .mark{background:var(--teal);width:34px;height:34px}
  .cover .photo{top:220px;height:420px;background:linear-gradient(170deg,#eef0ec 0%,#b7b09a 45%,#6f6a52 75%,#48513c 100%)}
  .cover .tagline{position:absolute;top:696px;left:24px;width:322px;text-align:center}
  .cover .tagline .sub{font-size:17px;color:var(--grey-text)}
  .cover .tagline .main{font:800 18px "Montserrat",Arial,sans-serif;color:var(--teal);letter-spacing:.5px;margin-top:4px}
  .cover .web{position:absolute;bottom:0;left:0;width:100%;height:50px;background:var(--black);color:var(--white);font-size:16px;letter-spacing:1px;text-align:center;padding-top:13px;border-top:4px solid var(--teal)}

  /* ---------- inside panels ---------- */
  .inside{background:var(--charcoal);color:var(--white)}
  .inside .photo{top:0;height:290px}
  .photo--scaffold{background:linear-gradient(150deg,#7fa3c6 0%,#b99470 45%,#6b5440 100%)}
  .photo--garage{background:linear-gradient(180deg,#d9d9d6 0%,#8f8f8c 50%,#5a5b58 100%)}
  .photo--balcony{background:linear-gradient(160deg,#e9ecef 0%,#c4c8cc 55%,#8e949a 100%)}
  .inside .heading{position:absolute;top:306px;left:0;width:100%;text-align:center}
  .inside .icon{display:block;margin:0 auto 6px;width:30px;height:30px}
  .inside h2{font:600 16px "Montserrat",Arial,sans-serif;letter-spacing:.5px;text-transform:uppercase}
  .inside .body{position:absolute;top:378px;left:30px;width:316px}
  .inside h3{font:700 13px "Montserrat",Arial,sans-serif;color:var(--teal);text-transform:uppercase;margin-top:8px}
  .inside ul{list-style:none;font-size:12px;line-height:1.5}
  .inside li{padding-left:12px;position:relative}
  .inside li::before{content:"•";position:absolute;left:0}
  .inside.misc ul{line-height:1.75}
  .inside .foot{position:absolute;bottom:0;left:0;width:100%;height:44px;background:var(--teal);color:var(--white);font:600 14px "Montserrat",Arial,sans-serif;letter-spacing:.5px;display:flex;align-items:center;justify-content:center;gap:8px}
</style>
</head>
<body>

<section class="spread spread--outside">

  <article class="panel services">
    <div class="photo" role="img" aria-label="Photograph of a finished mid-rise apartment building at dusk"></div>
    <svg class="deco" style="top:0" height="320" viewBox="0 0 370 320" preserveAspectRatio="none">
      <path d="M0 0 H370 V28 Q190 10 0 44 Z" fill="#1b1b1b"/>
      <path d="M0 280 Q190 250 370 200 V320 H0 Z" fill="#f4f4f4"/>
      <path d="M0 280 Q190 250 370 200" fill="none" stroke="#16a58d" stroke-width="5"/>
    </svg>
    <div class="tab">SERVICES</div>
    <p class="intro">We restore aging residential and commercial properties across the region, helping owners protect, repair and renew every structure.</p>
    <ul>
      <li>Structural Repairs</li>
      <li>Building Envelope Repairs</li>
      <li>Parking Garage Repairs</li>
      <li>Concrete and Masonry Work</li>
      <li>Balcony Restoration</li>
      <li>Waterproofing Systems</li>
      <li>Sealant Replacement</li>
      <li>Engineering Testing</li>
      <li>Cosmetic Repairs</li>
    </ul>
    <div class="foot">SCHEDULE YOUR FREE ESTIMATE</div>
  </article>

  <article class="panel about">
    <svg class="deco" style="top:0" height="120" viewBox="0 0 370 120" preserveAspectRatio="none">
      <path d="M0 0 H370 V40 Q180 110 0 60 Z" fill="#1b1b1b"/>
    </svg>
    <div class="circle-photo" role="img" aria-label="Photograph of architectural plans and drafting tools on a desk"></div>
    <div class="brand"><span class="mark"></span><span>MERIDIAN RESTORATION CORP</span></div>
    <p class="p1">We deliver reliable repair and restoration for owners, managers and boards, keeping every building safe, sound and looking its very best for years to come.</p>
    <p class="p2">Our team brings skilled crews, clear pricing and careful planning to each project, so your work is finished on time and to the highest standard.</p>
    <div class="cta">Schedule your free consultation for your next project</div>
    <div class="social" aria-label="Social links"><span></span><span></span><span></span><span></span></div>
    <svg class="deco" style="bottom:0" height="130" viewBox="0 0 370 130" preserveAspectRatio="none">
      <path d="M0 60 Q200 20 370 70 V130 H0 Z" fill="#1b1b1b"/>
      <path d="M0 60 Q200 20 370 70" fill="none" stroke="#ffffff" stroke-width="3"/>
    </svg>
    <div class="phone-bar">
      <svg width="20" height="20" viewBox="0 0 24 24"><circle cx="12" cy="12" r="11" fill="none" stroke="#16a58d" stroke-width="2"/><path d="M8 6.5l2 .2.8 2.6-1.3 1a6 6 0 0 0 3.2 3.2l1-1.3 2.6.8.2 2c-4.5.6-9.6-4.5-8.5-8.5z" fill="#16a58d"/></svg>
      <span>0198 765 432</span>
    </div>
  </article>

  <article class="panel cover">
    <div class="brand"><span class="mark"></span><span>MERIDIAN<br>RESTORATION CORP</span></div>
    <div class="photo" role="img" aria-label="Rendering of a modern residential building with balconies and trees"></div>
    <svg class="deco" style="top:150px" height="120" viewBox="0 0 370 120" preserveAspectRatio="none">
      <path d="M0 20 Q180 110 370 10 V0 H0 Z" fill="#ffffff"/>
      <path d="M0 20 Q180 110 370 10 V40 Q180 130 0 46 Z" fill="#1b1b1b"/>
    </svg>
    <svg class="deco" style="top:580px" height="110" viewBox="0 0 370 110" preserveAspectRatio="none">
      <path d="M0 70 Q190 20 370 50 V110 H0 Z" fill="#ffffff"/>
      <path d="M0 70 Q190 20 370 50" fill="none" stroke="#16a58d" stroke-width="5"/>
    </svg>
    <div class="tagline">
      <div class="sub">Residential and Commercial</div>
      <div class="main">REPAIR • REBUILD • RESTORE</div>
    </div>
    <div class="web">www.meridianrestore.com</div>
  </article>
</section>

<section class="spread spread--inside">

  <article class="panel inside">
    <div class="photo photo--scaffold" role="img" aria-label="Photograph of scaffolding on a building facade"></div>
    <svg class="deco" style="top:230px" height="80" viewBox="0 0 370 80" preserveAspectRatio="none">
      <path d="M0 40 Q190 10 370 40 V80 H0 Z" fill="#2a2a2a"/>
      <path d="M0 40 Q190 10 370 40" fill="none" stroke="#16a58d" stroke-width="5"/>
    </svg>
    <div class="heading">
      <svg class="icon" viewBox="0 0 30 30"><rect x="2" y="2" width="26" height="26" fill="#16a58d"/><path d="M8 23V11l7-4 7 4v12" fill="none" stroke="#fff" stroke-width="2"/></svg>
      <h2>Building Envelope</h2>
    </div>
    <div class="body">
      <h3>Concrete Repairs</h3>
      <ul><li>Balcony slabs</li><li>Shear Walls</li><li>Beams &amp; Columns</li></ul>
      <h3>Masonry Repairs</h3>
      <ul><li>Brick, Block &amp; Stone replacement</li><li>Tuck pointing</li><li>Through wall flashing</li><li>Coating (Elastomeric, Silicone and Architectural coatings)</li></ul>
      <h3>Sealant Replacement</h3>
      <ul><li>Window wall and glazing system sealants</li><li>Precast sealants</li><li>Masonry perimeter joints</li></ul>
      <h3>Waterproofing</h3>
      <ul><li>Balconies &amp; Terraces thin system</li><li>Garbage &amp; Mechanical rooms</li></ul>
    </div>
    <div class="foot">SCHEDULE YOUR FREE ESTIMATE</div>
  </article>

  <article class="panel inside">
    <div class="photo photo--garage" role="img" aria-label="Photograph of an underground parking garage with columns and caution tape"></div>
    <svg class="deco" style="top:230px" height="80" viewBox="0 0 370 80" preserveAspectRatio="none">
      <path d="M0 40 Q190 10 370 40 V80 H0 Z" fill="#2a2a2a"/>
      <path d="M0 40 Q190 10 370 40" fill="none" stroke="#16a58d" stroke-width="5"/>
    </svg>
    <div class="heading">
      <svg class="icon" viewBox="0 0 30 30"><rect x="2" y="2" width="26" height="26" fill="#16a58d"/><path d="M7 23V12l8-5 8 5v11M11 23v-7h8v7" fill="none" stroke="#fff" stroke-width="2"/></svg>
      <h2>Parking Garage Structures</h2>
    </div>
    <div class="body">
      <h3>Concrete Repairs</h3>
      <ul><li>Partial slab replacement</li><li>Top/under side repairs</li><li>Topside demolition</li><li>Catch basins &amp; trench drains</li><li>Columns, Beams and Shear walls</li></ul>
      <h3>Waterproofing</h3>
      <ul><li>Vehicular thin system (drive aisles, ramps, etc.)</li><li>Hot applied waterproofing (Roofs and Roof decks)</li><li>Expansion joints repair/replacement</li><li>Mastic waterproofing system</li><li>Foundation waterproofing</li><li>Crystalline waterproofing</li></ul>
      <h3>Ramp Heating</h3>
      <ul><li>Electric heating cables</li><li>Asphalt, interlocking, Mastic and Concrete</li></ul>
    </div>
    <div class="foot">
      <svg width="18" height="18" viewBox="0 0 24 24"><circle cx="12" cy="12" r="11" fill="none" stroke="#fff" stroke-width="2"/><path d="M8 6.5l2 .2.8 2.6-1.3 1a6 6 0 0 0 3.2 3.2l1-1.3 2.6.8.2 2c-4.5.6-9.6-4.5-8.5-8.5z" fill="#fff"/></svg>
      <span>0198 765 432</span>
    </div>
  </article>

  <article class="panel inside misc">
    <div class="photo photo--balcony" role="img" aria-label="Photograph of restored white balconies with railings"></div>
    <svg class="deco" style="top:230px" height="80" viewBox="0 0 370 80" preserveAspectRatio="none">
      <path d="M0 40 Q190 10 370 40 V80 H0 Z" fill="#2a2a2a"/>
      <path d="M0 40 Q190 10 370 40" fill="none" stroke="#16a58d" stroke-width="5"/>
    </svg>
    <div class="heading">
      <svg class="icon" viewBox="0 0 30 30"><rect x="2" y="2" width="26" height="26" fill="#16a58d"/><path d="M8 21h14M10 21v-8h10v8M15 13V8" fill="none" stroke="#fff" stroke-width="2"/></svg>
      <h2>Miscellaneous</h2>
    </div>
    <div class="body">
      <ul>
        <li>Balcony remediation and replacement</li>
        <li>Outside garbage and enclosures</li>
        <li>Retaining wall repair/replacement</li>
        <li>Stripping and railing systems</li>
        <li>Safety bollards &amp; precast curbs installation</li>
        <li>Side walks, curbs, interlocking, asphalt and landscape</li>
        <li>Balconies and Parking garages painting</li>
        <li>Area drains replacements</li>
        <li>Etc.</li>
      </ul>
    </div>
    <div class="foot">www.meridianrestore.com</div>
  </article>
</section>

</body>
</html>
```